New Architectural Firm Business Cards

New Business card to compliment previous pixel forum logo (attached). Please design a business card that is simple, modern, creative....please do not use "symbols", simply the logo and associated graphics/text. The front should contain name/address/phone/email/web address (with graphics).....back should be 100% graphic design using the logo somehow. Hoping for a two color (black and yellow) design. full bleed design, no borders

Target Market(s)

Commercial Architecture Clients

Industry/Entity Type

Architecture

Contact Information for Business Card

Please design a business card that is simple, modern, creative....please do not use "symbols", simply the logo and associated graphics/text. The front should contain name/address/phone/email/web address (with graphics).....back should be 100% graphic design using the logo somehow

Font styles to use
Sans Serif

Colors
FFF300
FFF600
FEFA6F
FFFEC7
FFFEE8

Requirements
Must have
• Clean, Modern Design
Should not have
• Stock images or "icons"

```html
<!DOCTYPE html>
<html lang="en">
<head>
<meta charset="utf-8">
<title>Pixel Forum Architecture – Business Card</title>
<link rel="stylesheet" href="https://fonts.googleapis.com/css2?family=Montserrat:wght@400;700;800&family=Roboto+Slab:wght@700&display=swap">
<style>
  :root {
    --backdrop: #aebfd1;
    --card-white: #ffffff;
    --brand-yellow: #f5c313;
    --ink: #2b2b2b;
    --soft-grey: #d0d0d0;
    --shadow: rgba(30, 40, 60, 0.28);
  }
  * { box-sizing: border-box; margin: 0; padding: 0; }
  html, body {
    width: 1200px; height: 900px; overflow: hidden;
    background: var(--backdrop);
    font-family: "Montserrat", sans-serif;
  }
  .canvas { position: relative; width: 1200px; height: 900px; }

  .card { position: absolute; overflow: hidden; box-shadow: 0 14px 30px var(--shadow); }

  /* Front */
  .card-front {
    left: 60px; top: 262px; width: 640px; height: 366px;
    background: var(--card-white);
  }
  .card-front .accent-circle {
    position: absolute; right: -120px; top: 70px;
    width: 330px; height: 330px; border-radius: 50%;
    background: var(--soft-grey);
  }
  .name-band {
    position: absolute; right: 0; top: 36px;
    width: 360px; height: 74px;
    background: var(--brand-yellow);
    clip-path: polygon(0 0, 100% 0, 100% 100%, 14% 100%);
    color: var(--card-white);
    padding: 12px 24px 0 92px;
    font-family: "Roboto Slab", serif;
  }
  .name-band .person-name { font-size: 25px; font-weight: 700; line-height: 1.1; }
  .name-band .person-role { font-size: 13px; font-weight: 700; margin-top: 3px; }

  .contact-list {
    position: absolute; left: 360px; top: 150px;
    list-style: none; color: var(--ink); font-size: 15px;
  }
  .contact-item { display: flex; align-items: center; gap: 18px; margin-bottom: 16px; }
  .contact-icon {
    flex: none; width: 34px; height: 34px; border-radius: 50%;
    background: var(--brand-yellow);
    display: flex; align-items: center; justify-content: center;
  }
  .contact-icon svg { width: 18px; height: 18px; }
  .contact-text { line-height: 1.3; letter-spacing: 0.3px; }

  .wordmark {
    position: absolute; left: 40px; bottom: 58px;
    color: var(--brand-yellow); font-weight: 800;
    display: flex; align-items: center; gap: 12px;
  }
  .wordmark .mark-dot { width: 26px; height: 26px; border-radius: 50%; background: var(--brand-yellow); }
  .wordmark .mark-name { font-size: 40px; line-height: 1; }
  .wordmark .mark-sub { font-size: 22px; letter-spacing: 1px; margin-top: 4px; }

  /* Back */
  .card-back {
    left: 790px; top: 190px; width: 300px; height: 525px;
    background: var(--brand-yellow);
    display: flex; flex-direction: column; align-items: center; justify-content: center; gap: 18px;
  }
  .card-back .mark-dot { width: 90px; height: 90px; border-radius: 50%; background: var(--card-white); }
  .card-back .mark-name {
    color: var(--card-white); font-weight: 800; font-size: 40px;
    line-height: 1.05; text-align: center;
  }
</style>
</head>
<body>
<main class="canvas">

  <section class="card card-front" aria-label="Business card front">
    <div class="accent-circle"></div>

    <div class="name-band">
      <div class="person-name">L.T Marlowe</div>
      <div class="person-role">Solution Manager</div>
    </div>

    <ul class="contact-list">
      <li class="contact-item">
        <span class="contact-icon">
          <svg viewBox="0 0 24 24" fill="#fff"><path d="M6.6 10.8a15.1 15.1 0 0 0 6.6 6.6l2.2-2.2a1 1 0 0 1 1-.25 11.4 11.4 0 0 0 3.6.57 1 1 0 0 1 1 1V20a1 1 0 0 1-1 1A17 17 0 0 1 3 4a1 1 0 0 1 1-1h3.5a1 1 0 0 1 1 1c0 1.25.2 2.45.57 3.57a1 1 0 0 1-.25 1z"/></svg>
        </span>
        <span class="contact-text">+00 700 120 345<br>+00 700 678 910</span>
      </li>
      <li class="contact-item">
        <span class="contact-icon">
          <svg viewBox="0 0 24 24" fill="none" stroke="#fff" stroke-width="2"><circle cx="12" cy="12" r="9"/><path d="M3 12h18M12 3c3 3.2 3 14.8 0 18M12 3c-3 3.2-3 14.8 0 18"/></svg>
        </span>
        <span class="contact-text">www.pixelforum-studio.com</span>
      </li>
      <li class="contact-item">
        <span class="contact-icon">
          <svg viewBox="0 0 24 24" fill="#fff"><path d="M2 11 22 3l-6 18-4-7z"/></svg>
        </span>
        <span class="contact-text">info@pixelforum-studio.com</span>
      </li>
    </ul>

    <div class="wordmark">
      <span class="mark-dot"></span>
      <div>
        <div class="mark-name">Pixel Forum</div>
        <div class="mark-sub">ARCHITECTURE</div>
      </div>
    </div>
  </section>

  <section class="card card-back" aria-label="Business card back">
    <span class="mark-dot"></span>
    <div class="mark-name">Pixel<br>Forum</div>
  </section>

</main>
</body>
</html>
```